BRIGHTWAVE PARTNERS NAMECARD

Need to design a name card with an existing logo.

As we are professional corporate services provider our name card has to project a professional image.
Should be corporate, simple & professional.

Our corporate color is maroon red but not too dull.

Please refer to our website at www.brightwavepartners.com.sg

Would attach our logo herewith.

Front surface of namecard details:
BRIGHTWAVE PARTNERS PTE LTD
Registration No. 208731945K

Lowe Hui Ting CA (Singapore)
Director

Tel +65 6481 2957
Mobile +65 9172 3806
lowe@brightwavepartners.com.sg
www.brightwavepartners.com.sg

47 Palmer Lane
#07-14 Harbourlight Plaza
Singapore 274153

Back of namecard:-
OUR CORE SERVICES
Incorporation services
Corporate Secretarial Services
Accountancy service
Goods & Services Taxation
Corporate & Personal Taxation
Financial Reporting
Payroll Administration

AFFILIATES:
TRIVANTA CORPORATE SERVICES PTE LTD
BRIGHTWAVEREGISTRYPTE LTD
ORR MANAGEMENT SERVICES PTE LTD
DW LIM AND COMPANY PTE LTD
LEDGERWISE ACADEMY

```html
<!DOCTYPE html>
<html lang="en">
<head>
<meta charset="utf-8">
<title>Brightwave Partners – Name Card</title>
<link rel="stylesheet" href="https://fonts.googleapis.com/css2?family=Open+Sans:wght@400;600&display=swap">
<style>
  :root {
    --red: #ff0000;
    --brand-red: #d4021d;
    --pink: #ff1f70;
    --maroon: #6a0606;
    --paper: #f4f5f7;
    --divider: #e6e7eb;
    --white: #ffffff;
    --ink: #1a1a1a;
    --icon: #8fe6ff;
  }
  html, body {
    margin: 0;
    padding: 0;
    width: 1200px;
    height: 720px;
    overflow: hidden;
    background: var(--paper);
  }
  .card {
    position: relative;
    width: 1200px;
    height: 720px;
    font-family: "Open Sans", Arial, sans-serif;
    overflow: hidden;
    background: var(--paper);
  }
  .top-field {
    position: absolute;
    left: 0;
    top: 0;
    width: 1200px;
    height: 360px;
    background: linear-gradient(100deg, var(--pink) 0%, var(--maroon) 38%, var(--red) 58%, var(--red) 100%);
  }
  .panel-divider {
    position: absolute;
    left: 610px;
    top: 360px;
    width: 2px;
    height: 303px;
    background: var(--divider);
  }
  .footer-band {
    position: absolute;
    left: 0;
    top: 663px;
    width: 1200px;
    height: 57px;
    background: var(--red);
  }
  .holder {
    position: absolute;
    left: 521px;
    top: 84px;
    color: var(--white);
  }
  .holder-name {
    font-size: 48px;
    font-weight: 400;
    line-height: 1;
    margin: 0;
    letter-spacing: 0.5px;
  }
  .holder-qualifier {
    font-size: 22px;
    letter-spacing: 0.5px;
    margin-left: 10px;
  }
  .holder-title {
    font-size: 26px;
    letter-spacing: 2px;
    margin: 10px 0 0 34px;
    line-height: 1;
  }
  .company {
    position: absolute;
    left: 757px;
    top: 250px;
    color: var(--white);
    font-size: 23px;
    letter-spacing: 1.6px;
    line-height: 32px;
    margin: 0;
  }
  .brand-name {
    position: absolute;
    left: 28px;
    top: 400px;
    margin: 0;
    color: var(--brand-red);
    font-weight: 600;
    font-size: 80px;
    line-height: 98px;
    letter-spacing: 1px;
  }
  .contact-list {
    position: absolute;
    left: 0;
    top: 0;
    margin: 0;
    padding: 0;
    list-style: none;
    color: var(--ink);
    font-size: 20px;
    letter-spacing: 1.4px;
  }
  .contact-item {
    position: absolute;
    left: 762px;
    line-height: 29px;
    white-space: nowrap;
  }
  .contact-phone { top: 382px; }
  .contact-email { top: 455px; }
  .contact-web { top: 514px; left: 767px; }
  .contact-address { top: 557px; left: 766px; }
  .contact-icons {
    position: absolute;
    left: 0;
    top: 0;
    width: 1200px;
    height: 720px;
    pointer-events: none;
  }
</style>
</head>
<body>
<main class="card">
  <div class="top-field" role="img" aria-label="Decorative diagonal pattern in pink, white, maroon and red"></div>
  <div class="panel-divider"></div>
  <div class="footer-band"></div>

  <svg class="contact-icons" viewBox="0 0 1200 720" aria-hidden="true">
    <g class="icon icon-phone" transform="translate(720 407)">
      <circle r="25" fill="var(--brand-red)"/>
      <path d="M-7,-10 l4,-1 3,6 -3,2 q2,5 6,8 l2,-3 6,3 -1,4 q-3,3 -8,1 q-8,-4 -11,-12 q-1,-5 2,-8z" fill="var(--icon)"/>
    </g>
    <g class="icon icon-mail" transform="translate(720 467)">
      <circle r="25" fill="var(--brand-red)"/>
      <rect x="-11" y="-7" width="22" height="14" fill="var(--icon)"/>
      <path d="M-11,-7 L0,2 L11,-7" fill="none" stroke="var(--brand-red)" stroke-width="2"/>
    </g>
    <g class="icon icon-web" transform="translate(720 527)">
      <circle r="25" fill="var(--brand-red)"/>
      <circle r="17" fill="none" stroke="var(--icon)" stroke-width="1.5"/>
      <ellipse rx="7" ry="17" fill="none" stroke="var(--icon)" stroke-width="1.5"/>
      <line x1="-17" y1="0" x2="17" y2="0" stroke="var(--icon)" stroke-width="1.5"/>
    </g>
    <g class="icon icon-pin" transform="translate(720 604)">
      <circle r="25" fill="var(--brand-red)"/>
      <path d="M0,12 L-7,0 A8,8 0 1 1 7,0 Z" fill="var(--icon)"/>
      <circle cy="-4" r="3" fill="var(--brand-red)"/>
    </g>
  </svg>

  <header class="holder">
    <h1 class="holder-name">LOWE HUI TING CA<span class="holder-qualifier">(SINGAPORE)</span></h1>
    <p class="holder-title">DIRECTOR</p>
  </header>

  <p class="company">BRIGHTWAVE PARTNERS PTE LTD<br>Registration No. 208731945K</p>

  <p class="brand-name">BRIGHTWAVE<br>PARTNERS</p>

  <ul class="contact-list">
    <li class="contact-item contact-phone">Tel +65 6481 2957<br>Mobile +65 9172 3806</li>
    <li class="contact-item contact-email">lowe@brightwavepartners.com.sg</li>
    <li class="contact-item contact-web">www.brightwavepartners.com.sg</li>
    <li class="contact-item contact-address">47 Palmer Lane<br>#07-14 Harbourlight Plaza<br>Singapore 274153</li>
  </ul>
</main>
</body>
</html>
```